Executive resume - bring a creative edge to an Executive Resume

I want this resume to stand out - front page is really critical.

Target Market(s)

Executive Job in Creative Industries

```html
<!DOCTYPE html>
<html lang="en">
<head>
<meta charset="utf-8">
<title>Rowan Hale — Executive Resume</title>
<link href="https://fonts.googleapis.com/css2?family=Didact+Gothic&family=Montserrat:wght@600;700;800&display=swap" rel="stylesheet">
<style>
  :root {
    --backdrop: #d4d4d4;
    --paper: #ffffff;
    --ink: #231f20;
    --ink-reverse: #ffffff;
    --date-panel: #d9d9da;
    --rule: #231f20;
  }
  * { margin: 0; padding: 0; box-sizing: border-box; }
  html, body { width: 1200px; height: 984px; overflow: hidden; }
  body {
    background: var(--backdrop);
    font-family: "Didact Gothic", "Century Gothic", sans-serif;
    color: var(--ink);
    position: relative;
  }
  .resume {
    position: absolute;
    left: 281px; top: 39px;
    width: 639px; height: 903px;
    background: var(--paper);
    overflow: hidden;
  }

  /* Header */
  .identity-bar {
    position: absolute; left: 0; top: 26px;
    width: 16px; height: 87px; background: var(--ink);
  }
  .identity {
    position: absolute; left: 24px; top: 45px;
    width: 124px;
    line-height: 1;
    white-space: nowrap;
  }
  .identity__name {
    font-family: "Montserrat", sans-serif;
    font-weight: 700; font-size: 16px; letter-spacing: -0.2px;
  }
  .identity__phone { font-size: 15px; margin-top: 3px; }
  .identity__email { font-size: 11.2px; margin-top: 2px; }
  .header-rule {
    position: absolute; left: 152px; top: 26px;
    width: 1px; height: 87px; background: var(--ink);
  }
  .profile {
    position: absolute; left: 161px; top: 23px; width: 458px;
    font-size: 9.9px; line-height: 12.4px; text-align: justify;
  }

  /* Dark band */
  .highlights {
    position: absolute; left: 0; top: 135px;
    width: 639px; height: 384px; background: var(--ink);
    color: var(--ink-reverse);
  }
  .highlights__heading {
    position: absolute; top: 10px; height: 21px;
    background: var(--paper); color: var(--ink);
    font-family: "Montserrat", sans-serif; font-weight: 700;
    font-size: 9.5px; letter-spacing: 0.3px;
    display: flex; align-items: center; justify-content: center;
  }
  .highlights__heading--achievements { left: 36px; width: 413px; }
  .highlights__heading--strengths { left: 469px; width: 143px; }
  .highlights__list {
    position: absolute; top: 37px;
    font-size: 10.2px; line-height: 11.9px; letter-spacing: 0.12px; list-style: none;
  }
  .highlights__list--achievements { left: 36px; width: 413px; text-align: justify; }
  .highlights__list--strengths { left: 469px; width: 140px; }
  .highlights__list li::before { content: "• "; }

  /* Timeline sections */
  .record { position: absolute; left: 0; width: 639px; }
  .record__heading {
    position: absolute; left: 36px; top: 0;
    font-family: "Montserrat", sans-serif; font-weight: 700;
    font-size: 10px; letter-spacing: 0.2px;
  }
  .record__dates-panel {
    position: absolute; left: 507px; width: 129px; background: var(--date-panel);
  }
  .record__rows { position: absolute; left: 36px; list-style: none; }
  .record__row {
    display: grid; grid-template-columns: 208px 267px 120px;
    font-size: 9.8px; line-height: 11.8px; white-space: nowrap;
  }
  .record__rule {
    position: absolute; left: 25px; width: 613px; height: 1.2px; background: var(--rule);
  }
  .footer-band {
    position: absolute; left: 0; bottom: 0; width: 639px; height: 16px; background: var(--ink);
  }
</style>
</head>
<body>
<main class="resume">
  <header>
    <div class="identity-bar"></div>
    <div class="identity">
      <h1 class="identity__name">ROWAN HALE</h1>
      <p class="identity__phone">+61 400 555 182</p>
      <p class="identity__email">rowanhale@mailbox.com</p>
    </div>
    <div class="header-rule"></div>
    <p class="profile">With a proven track record in governance, executive and senior leadership positions, I am an established transformative thought leader, a strategic storyteller, and an experienced change management leader. Having maintained a creative and interdisciplinary career across multiple sectors and industries, my professional experience has included work in education, the arts and creative industries, agriculture, music, media and broadcasting industries, and in community, youth and cultural development. I have secured and maintained a national and international reputation as a facilitator who designs and presents successful frameworks for guiding strategic, collaborative and urgent conversations into action.</p>
  </header>

  <section class="highlights">
    <h2 class="highlights__heading highlights__heading--achievements">RECENT ACHIEVEMENTS</h2>
    <ul class="highlights__list highlights__list--achievements">
      <li>C-Suite executive leadership within an international private higher education context.</li>
      <li>Head of school leadership experience in a regional public university context.</li>
      <li>Leadership of a division driving engagement, including internal, executive, employability and industry engagement, external communication and public relations and a wide range of social impact initiatives across a university of 16,000 students and 1,700 staff members. This includes stewardship of the company’s B Corporation, demonstrating that business can both be for-profit and for-purpose while making an enduring contribution to individuals, communities and countries.</li>
      <li>Leadership of communications, media relations, B Corporation, social impact and thought leadership initiatives as the company spokesperson reporting to the CEO. Stakeholders included the board, C-level executives, investor relations, global network university leaders, partner organizations and the media.</li>
      <li>Leadership and development of a complex national co-design process to establish an industry roadmap and strategic agenda to grow an industry from $60 billion to $100 billion dollars by 2030. This process has also led to the development of a 12-year strategic plan for the national peak body.</li>
      <li>Leadership of an entirely new curriculum development process for a creative arts school in a higher education context.</li>
      <li>Facilitation of national and international co-design processes, summits and consultations that have led to significant and sustained local agendas, national agendas and international agendas.</li>
      <li>Consultation as advisor to chief executive officers, chairmen, boards of management and executives of large public organisations, private commercial organisations, state government agencies, local councils and community-based not-for-profit enterprises.</li>
      <li>Consistent production of outstanding results where it most matters—trusted peer relationships, great customer experiences, loyal and energised people, innovative products and, ultimately, a more successful enterprise.</li>
    </ul>

    <h2 class="highlights__heading highlights__heading--strengths">STRENGTHS</h2>
    <ul class="highlights__list highlights__list--strengths">
      <li>Leading cultural change, stakeholder management and engagement.</li>
      <li>Strategic communication using storytelling as a means of transformation and change.</li>
      <li>Facilitating communication, engagement and cultural turnarounds resulting in greater productivity, engagement and results.</li>
      <li>Global business management, working with culturally diverse teams and a global network.</li>
      <li>Initiating and managing large-scale multi-million-dollar programs and projects.</li>
      <li>Strategic and innovative thinking with a demonstrated track record.</li>
      <li>Proven ability to catalyse and manage change.</li>
    </ul>
  </section>

  <section class="record" style="top:529px">
    <h2 class="record__heading">KEY PROFESSIONAL EXPERIENCE</h2>
    <div class="record__dates-panel" style="top:16px;height:61px"></div>
    <ul class="record__rows" style="top:17px">
      <li class="record__row"><span>Meridian Global Universities</span><span>Vice President of Communications and Public Affairs</span><span>Jan 2019 – Present</span></li>
      <li class="record__row"><span>National Broadcasting Network</span><span>Chief Facilitator – Outpost Regional Youth Program</span><span>Mar 2010 – Present</span></li>
      <li class="record__row"><span>Harvest Futures Network</span><span>Consultant – Leadership and Sector Development</span><span>Jan 2010 – Present</span></li>
      <li class="record__row"><span>Goldfields University</span><span>Director – Goldfields Arts Academy and GSD</span><span>Jan 2017 – Feb 2018</span></li>
      <li class="record__row"><span>National Broadcasting Network</span><span>Executive Producer – Rural and Regional</span><span>Apr 2007 – Mar 2010</span></li>
    </ul>
  </section>
  <div class="record__rule" style="top:613px"></div>

  <section class="record" style="top:623px">
    <h2 class="record__heading">KEY CONSULTANCY ENGAGEMENT</h2>
    <div class="record__dates-panel" style="top:12px;height:65px"></div>
    <ul class="record__rows" style="top:15px">
      <li class="record__row"><span>National Growers’ Alliance</span><span>Consultant and Advisor – Horizon 2030</span><span>Feb 2018 – Sep 2019</span></li>
      <li class="record__row"><span>Riverbend Rural City Council</span><span>Creative Industries and Cultural Development Advisor</span><span>Feb 2017 – Present</span></li>
      <li class="record__row"><span>Music Southland</span><span>Strategy Consultant</span><span>2018</span></li>
      <li class="record__row"><span>National Growers’ Alliance</span><span>Strategy Facilitator – Digital Data Stewardship</span><span>2018</span></li>
      <li class="record__row"><span>Northern Broadcasting Service</span><span>Senior Media Training – Tanzania Elections Project</span><span>2015</span></li>
    </ul>
  </section>
  <div class="record__rule" style="top:702px"></div>

  <section class="record" style="top:710px">
    <h2 class="record__heading">BOARD DIRECTOR AND HONORARY ROLES</h2>
    <div class="record__dates-panel" style="top:12px;height:77px"></div>
    <ul class="record__rows" style="top:15px">
      <li class="record__row"><span>Lakeside Youth Arts Festival</span><span>Chairman of Advisory Board</span><span>Jan 2020 – Present</span></li>
      <li class="record__row"><span>City of Kestrel Creative City Strategy</span><span>Advisor</span><span>Jan 2017 – Dec 2019</span></li>
      <li class="record__row"><span>Community Radio Foundation</span><span>Foundation Director</span><span>May 2012 – Nov 2016</span></li>
      <li class="record__row"><span>Campus Youth Network Inc</span><span>Chairman of the Board</span><span>Sep 2008 – Apr 2010</span></li>
      <li class="record__row"><span>Community Radio Association</span><span>Board Member</span><span>Nov 2003 – Nov 2008</span></li>
      <li class="record__row"><span>Emerging Writers Media</span><span>Board Member</span><span>Nov 2005 – Nov 2007</span></li>
    </ul>
  </section>
  <div class="record__rule" style="top:809px"></div>

  <section class="record" style="top:814px">
    <h2 class="record__heading">ACADEMIC QUALIFICATIONS</h2>
    <div class="record__dates-panel" style="top:12px;height:32px"></div>
    <ul class="record__rows" style="top:14px">
      <li class="record__row"><span>National Academy of Theatre Arts</span><span>Master of Fine Arts (Cultural Leadership)</span><span>Currently in Progress</span></li>
      <li class="record__row"><span>University of Eastvale</span><span>Postgraduate Diploma in Performance Creation</span><span>2010</span></li>
    </ul>
  </section>

  <div class="footer-band"></div>
</main>
</body>
</html>
```